Acrylschild für Eingang
Zielgruppe
Projekt Acrylschild für Eingang
Wir sind ein Einzelhandel und Online-Shop im Bereich Wohnaccessoires und Mode im nordischen Stil. Unsere Zielgruppe sind eher Frauen von 20 bis 60 Jahren, trendbewußt und fit im Bereich Social Medias.
Aufgabenstellung
Grundsätzlich ist unser Motto: clean, nordisch, minimalistisch
Das Design sollte daher nur die wichtigsten Informationen enthalten und sich von der Optik bzw. den Schriftzügen an unseren Online-Shops orientieren. Auf jeden Fall nicht verspielt.
Das Projekt betrifft das Design eines Firmen Acrylschilds mit den Maßen 22 cm x 22 cm, dabei sollte beachtet werden, dass an den vier Ecken Befestigungen aus Edelstahl ihren Platz finden müssen.
Das Schild wird außen am Eingang auf Augenhöhe befestigt.
Darauf sollten folgende Informationen Platz finden:
- Logo
- der Text: nordic living
- Öffnungszeiten: Montag bis Samstag 10 bis 17 Uhr
- Telefonnummer: 07418 5126047
- Adresse Online-Shop: www.4heimform.de
...und eventuell als Möglichkeit ein QR-Code des Online-Shops
Das Logo und der Text nordic living (der auch klein geschrieben sein kann, eventuell auch kalligrafisch aber ohne Schnörkel z. B. ähnlich Schrift MINA) sollte 1 Bereich einnehmen
und etwas getrennt von den weiteren Informationen dargestellt werden.
Das Schild sollte nicht bunt oder farbige Hintergründe haben (die Wand dahinter ist in einem gebrochenen Weißton mit leicht rauher Struktur).

```html
<!DOCTYPE html>
<html lang="de">
<head>
<meta charset="utf-8">
<title>Kjellby – Eingangsschild</title>
<link rel="stylesheet" href="https://fonts.googleapis.com/css2?family=Fira+Sans+Condensed:wght@300;400;500&family=Quicksand:wght@400&display=swap">
<style>
  :root {
    --page: #f3f3f3;
    --sign: #ffffff;
    --ink: #1c1c1c;
    --ink-soft: #33393b;
  }
  html, body {
    margin: 0;
    padding: 0;
    width: 1200px;
    height: 2400px;
    overflow: hidden;
    background: var(--page);
  }
  .sign {
    position: absolute;
    left: 50px;
    top: 650px;
    width: 1100px;
    height: 1100px;
    background: var(--sign);
    box-shadow: 0 6px 30px rgba(0,0,0,0.08);
    font-family: "Fira Sans Condensed", "Arial Narrow", sans-serif;
    color: var(--ink);
    text-align: center;
  }
  .brand-name {
    position: absolute;
    left: 0;
    right: 0;
    top: 250px;
    margin: 0;
    font-family: "Fira Sans Condensed", "Arial Narrow", sans-serif;
    font-weight: 400;
    font-size: 160px;
    letter-spacing: 14px;
    line-height: 1;
    color: var(--ink);
  }
  .tagline {
    position: absolute;
    left: 0;
    right: 0;
    top: 520px;
    margin: 0;
    font-family: "Quicksand", sans-serif;
    font-weight: 400;
    font-size: 150px;
    line-height: 1;
    letter-spacing: 2px;
    color: var(--ink-soft);
  }
  .details {
    position: absolute;
    left: 0;
    right: 0;
    top: 735px;
    margin: 0;
  }
  .detail-label {
    display: block;
    font-weight: 500;
    font-size: 30px;
    letter-spacing: 1.5px;
    line-height: 1;
    margin: 0 0 10px;
  }
  .detail-value {
    display: block;
    font-weight: 300;
    font-size: 48px;
    letter-spacing: 1.5px;
    line-height: 1;
    margin: 0 0 30px;
  }
</style>
</head>
<body>
  <main class="sign">
    <p class="brand-name">KJELLBY</p>

    <p class="tagline">nordic living</p>

    <dl class="details">
      <dt class="detail-label">ÖFFNUNGSZEITEN:</dt>
      <dd class="detail-value">Montag bis Samstag von 10 bis 17 Uhr</dd>
      <dt class="detail-label">TELEFONNUMMER:</dt>
      <dd class="detail-value">07418 5126047</dd>
      <dt class="detail-label">ONLINE-SHOP:</dt>
      <dd class="detail-value">www.4heimform.de</dd>
    </dl>
  </main>
</body>
</html>
```